business cards and stationary
Vantor Motion Collective
Professional
Matthew L. Dorsand, D.C.
Chiropractor
4817 Halvering Crest Avenue
Los Angeles, CA 90048
mldorsand@vantormotion.example
Vantormotion.example
CA74829
map of location
logo file .AI

```html
<!DOCTYPE html>
<html lang="en">
<head>
<meta charset="utf-8">
<title>Vantor Motion Collective — Stationery Set</title>
<link rel="stylesheet" href="https://fonts.googleapis.com/css2?family=Open+Sans:wght@400;600;700;800&display=swap">
<style>
  :root {
    --stage: #3b3b3b;
    --stage-dark: #2a2a2a;
    --orange: #f7941d;
    --orange-deep: #e0780e;
    --grey: #7d7d7d;
    --grey-light: #d9d9d9;
    --paper: #ffffff;
    --ink: #4a4a4a;
    --label: #bdbdbd;
  }
  * { box-sizing: border-box; margin: 0; padding: 0; }
  html, body { width: 1200px; height: 437px; overflow: hidden; }
  body {
    position: relative;
    background: radial-gradient(ellipse at 50% 40%, var(--stage) 0%, var(--stage-dark) 100%);
    font-family: "Open Sans", Arial, sans-serif;
    color: var(--ink);
  }
  .piece { position: absolute; background: var(--paper); overflow: hidden; box-shadow: 0 2px 6px rgba(0,0,0,.45); }
  .piece svg.art { position: absolute; inset: 0; width: 100%; height: 100%; }
  .caption { position: absolute; font-size: 6px; color: var(--label); text-align: center; letter-spacing: .2px; }
  .set-title { position: absolute; left: 19px; top: 40px; font-size: 6px; color: var(--label); }

  .logo { position: absolute; display: flex; align-items: center; gap: 3px; font-weight: 800; color: var(--orange); line-height: 1; letter-spacing: -.3px; }
  .logo .dot { width: .45em; height: .45em; border-radius: 50%; background: var(--grey); }
  .logo.on-orange { color: var(--paper); }
  .logo.on-orange .dot { background: var(--paper); }
  .tagline { position: absolute; font-size: 4px; color: var(--grey); letter-spacing: .8px; text-transform: uppercase; }

  .tiny { position: absolute; font-size: 3.6px; line-height: 1.5; color: var(--ink); }
  .tiny strong { font-weight: 700; font-size: 4.4px; }

  /* business cards */
  .card-front { left: 19px; top: 53px; width: 178px; height: 96px; }
  .card-map { left: 19px; top: 173px; width: 178px; height: 115px; background: linear-gradient(135deg, #e6e2d8, #d5d9cc 55%, #c9d3dd); }
  .card-back { left: 19px; top: 312px; width: 178px; height: 92px; background: var(--orange); }

  /* letterheads */
  .letterhead-a { left: 216px; top: 24px; width: 266px; height: 396px; }
  .letterhead-b { left: 509px; top: 24px; width: 268px; height: 396px; }

  /* envelopes */
  .envelope { left: 811px; width: 360px; height: 72px; }
  .env-grey { top: 96px; }
  .env-orange { top: 173px; }
  .env-white { top: 254px; }
  .env-front { top: 336px; height: 80px; }
  .env-card { position: absolute; left: 822px; top: 368px; width: 100px; height: 54px; background: var(--orange); box-shadow: 0 2px 5px rgba(0,0,0,.4); overflow: hidden; }
  .env-card svg { position: absolute; inset: 0; width: 100%; height: 100%; }
</style>
</head>
<body>

  <div class="set-title">Business Cards (2)</div>

  <!-- Business card front -->
  <section class="piece card-front">
    <svg class="art" viewBox="0 0 178 96" preserveAspectRatio="none" aria-hidden="true">
      <path d="M178 0 V28 C150 14 120 8 90 10 C120 2 150 0 178 0Z" fill="var(--orange)"/>
      <path d="M178 0 H120 C140 2 162 8 178 18Z" fill="var(--orange-deep)"/>
      <path d="M0 96 V80 C40 92 90 94 140 86 C100 98 40 98 0 96Z" fill="var(--grey-light)"/>
    </svg>
    <div class="tiny" style="right:8px;top:20px;text-align:right;">
      <strong>Matthew L. Dorsand, D.C.</strong><br>Chiropractor · CA74829
    </div>
    <div class="logo" style="left:12px;top:44px;font-size:17px;">Vantor<span class="dot"></span></div>
    <div class="tagline" style="left:13px;top:63px;">Motion Collective</div>
    <div class="tiny" style="left:12px;top:72px;">
      4817 Halvering Crest Avenue, Los Angeles, CA 90048<br>
      P (310) 555-0148 · mldorsand@vantormotion.example
    </div>
  </section>
  <div class="caption" style="left:19px;top:152px;width:178px;">Front Card</div>

  <!-- Map card -->
  <section class="piece card-map" role="img" aria-label="Street map showing the clinic location in Los Angeles"></section>
  <div class="caption" style="left:19px;top:291px;width:178px;">Map Card</div>

  <!-- Business card back -->
  <section class="piece card-back">
    <svg class="art" viewBox="0 0 178 92" preserveAspectRatio="none" aria-hidden="true">
      <path d="M0 92 V66 C50 84 110 86 178 70 V92Z" fill="var(--paper)"/>
      <path d="M0 66 C50 84 110 86 178 70 V74 C110 90 50 88 0 72Z" fill="var(--grey)"/>
    </svg>
    <div class="logo on-orange" style="left:50px;top:26px;font-size:20px;">Vantor<span class="dot"></span></div>
    <div class="tiny" style="left:0;right:0;top:78px;text-align:center;">Vantormotion.example</div>
  </section>
  <div class="caption" style="left:19px;top:407px;width:178px;">Back Card</div>

  <!-- Letterhead A -->
  <section class="piece letterhead-a">
    <svg class="art" viewBox="0 0 266 396" preserveAspectRatio="none" aria-hidden="true">
      <path d="M266 0 V34 C230 16 190 8 140 10 C190 0 230 0 266 0Z" fill="var(--orange)"/>
      <path d="M266 34 C230 16 190 8 140 10 C190 6 232 14 266 28Z" fill="var(--grey)"/>
      <path d="M0 396 V360 C36 380 80 390 130 390 C80 396 36 396 0 396Z" fill="var(--orange)"/>
      <path d="M0 360 C36 380 80 390 130 390 C80 392 36 384 0 366Z" fill="var(--grey)"/>
    </svg>
    <div class="logo" style="left:18px;top:24px;font-size:20px;">Vantor<span class="dot"></span></div>
    <div class="tagline" style="left:19px;top:45px;">Motion Collective</div>
    <div class="tiny" style="left:112px;top:22px;">
      4817 Halvering Crest Avenue<br>Los Angeles, CA 90048
    </div>
    <div class="tiny" style="left:176px;top:22px;">
      P (310) 555-0148<br>F (310) 555-0149<br>Vantormotion.example
    </div>
  </section>
  <div class="caption" style="left:216px;top:423px;width:266px;">Letterhead A</div>

  <!-- Letterhead B -->
  <section class="piece letterhead-b">
    <svg class="art" viewBox="0 0 268 396" preserveAspectRatio="none" aria-hidden="true">
      <path d="M268 0 V40 C236 18 196 10 150 12 C196 0 236 0 268 0Z" fill="var(--orange)"/>
      <path d="M268 40 C236 18 196 10 150 12 C196 8 238 18 268 32Z" fill="var(--grey)"/>
      <path d="M0 396 V352 C40 378 90 388 150 388 C90 396 40 396 0 396Z" fill="var(--orange)"/>
      <path d="M0 352 C40 378 90 388 150 388 C90 390 40 380 0 358Z" fill="var(--grey)"/>
    </svg>
    <div class="logo" style="left:100px;top:26px;font-size:22px;">Vantor<span class="dot"></span></div>
    <div class="tagline" style="left:104px;top:50px;">Motion Collective</div>
    <div class="tiny" style="left:0;right:0;top:58px;text-align:center;">
      4817 Halvering Crest Avenue · Los Angeles, CA 90048 · P (310) 555-0148 · Vantormotion.example
    </div>
    <div class="tiny" style="left:0;right:0;top:382px;text-align:center;">mldorsand@vantormotion.example</div>
  </section>
  <div class="caption" style="left:509px;top:423px;width:268px;">Letterhead B</div>

  <div class="caption" style="left:1040px;top:86px;width:130px;text-align:right;">Envelope Front &amp; Back</div>

  <!-- Envelope back, grey flap -->
  <section class="piece envelope env-grey">
    <svg class="art" viewBox="0 0 360 72" preserveAspectRatio="none" aria-hidden="true">
      <path d="M0 0 H360 L200 36 H160Z" fill="var(--grey)"/>
      <path d="M0 72 L160 40 H200 L360 72" fill="none" stroke="var(--grey-light)" stroke-width="1"/>
    </svg>
    <div class="tiny" style="left:0;right:0;top:14px;text-align:center;color:#eee;">Vantormotion.example</div>
  </section>

  <!-- Envelope back, orange flap -->
  <section class="piece envelope env-orange">
    <svg class="art" viewBox="0 0 360 72" preserveAspectRatio="none" aria-hidden="true">
      <path d="M0 0 H360 L200 40 H160Z" fill="var(--orange)"/>
      <path d="M0 72 L160 44 H200 L360 72" fill="none" stroke="var(--grey-light)" stroke-width="1"/>
    </svg>
    <div class="tiny" style="left:0;right:0;top:16px;text-align:center;color:#fff;">Vantormotion.example</div>
  </section>

  <!-- Envelope back, white flap -->
  <section class="piece envelope env-white">
    <svg class="art" viewBox="0 0 360 72" preserveAspectRatio="none" aria-hidden="true">
      <path d="M0 0 H360 L200 38 H160Z" fill="#f4f4f4" stroke="var(--grey-light)" stroke-width="1"/>
      <path d="M0 72 L160 42 H200 L360 72" fill="none" stroke="var(--grey-light)" stroke-width="1"/>
    </svg>
  </section>

  <!-- Envelope front -->
  <section class="piece envelope env-front">
    <svg class="art" viewBox="0 0 360 80" preserveAspectRatio="none" aria-hidden="true">
      <path d="M0 80 V52 C50 70 110 76 170 72 C110 82 50 82 0 80Z" fill="var(--orange)"/>
      <path d="M0 52 C50 70 110 76 170 72 C110 74 50 66 0 56Z" fill="var(--grey)"/>
    </svg>
    <div class="tiny" style="left:200px;top:34px;">
      Matthew L. Dorsand, D.C.<br>4817 Halvering Crest Avenue<br>Los Angeles, CA 90048
    </div>
  </section>

  <!-- Card laid over envelope -->
  <div class="env-card">
    <svg viewBox="0 0 100 54" preserveAspectRatio="none" aria-hidden="true">
      <path d="M0 54 V40 C30 50 66 50 100 42 V54Z" fill="var(--paper)"/>
    </svg>
    <div class="logo on-orange" style="left:22px;top:14px;font-size:15px;">Vantor<span class="dot"></span></div>
  </div>

</body>
</html>
```